KV HOLDING Business Cards

I need business cards for "KV Holding group LLC" doublesided... logo on the back (also include logo on front)
logo attached to project... i have jpg up..
Company Info:
418 East Marlow Avenue, Suite 7B
Chicago, Illinois 60617
facsimile 312-555-0188 (list fax, address, website on all cards.)
www.kvholdinggroup.example
Three different people on cards:
Dorian P. Kell, CPA MST
Principal
ofc 312-555-0142
mobile 312-555-0167
dorianpkell@kvholdinggroup.example
Marcus T. Brenholt, CPA MST
Principal
marcustbrenholt@kvholdinggroup.example
mobile 708-555-0119
ofc 312-555-0142
Nigel F Carrow
Principal
ofc 312-555-0142
no mobile
nigelfcarrow@kvholdinggroup.example
I have multiple projects listed.. see below:
Business cards for amber gate equity llc
letterhead
envelopes
Business cards for KV Holding LLC
letterhead
envelopes
Target Market(s)
rich people
Industry/Entity Type
Business
Look and feel

```html
<!DOCTYPE html>
<html lang="en">
<head>
<meta charset="utf-8">
<title>KV Holding Group LLC — Business Card</title>
<link href="https://fonts.googleapis.com/css2?family=Exo+2:wght@400;600;700&display=swap" rel="stylesheet">
<style>
  :root {
    --navy: #1d4a86;
    --navy-dark: #173d70;
    --paper: #fbfbfb;
    --panel: #f4f4f5;
    --map: #dcdde0;
    --icon: #8e9196;
    --stage: #e6e7e9;
  }
  * { box-sizing: border-box; margin: 0; padding: 0; }
  html, body { width: 1200px; height: 1119px; overflow: hidden; }
  body {
    background: var(--stage);
    font-family: "Exo 2", sans-serif;
    color: var(--navy);
    position: relative;
  }
  .card {
    position: absolute;
    left: 150px;
    width: 900px;
    height: 514px;
    background: var(--paper);
    box-shadow: 0 2px 10px rgba(0,0,0,0.12);
    overflow: hidden;
  }
  .card--back { top: 30px; }
  .card--front { top: 575px; }

  .world-map {
    position: absolute;
    inset: 40px 30px 30px 30px;
    background: radial-gradient(ellipse at 35% 45%, var(--map) 0%, rgba(220,221,224,0.55) 45%, rgba(220,221,224,0) 75%);
    opacity: 0.8;
  }

  /* back */
  .back-brand {
    position: absolute;
    top: 170px; left: 0; right: 0;
    display: flex; align-items: center; justify-content: center; gap: 22px;
  }
  .brand-dot {
    flex: none;
    border-radius: 50%;
    background: var(--navy);
  }
  .back-brand .brand-dot { width: 70px; height: 70px; }
  .brand-name {
    font-weight: 600;
    color: var(--navy);
    letter-spacing: 0.04em;
    white-space: nowrap;
  }
  .back-brand .brand-name { font-size: 52px; }
  .back-web {
    position: absolute;
    top: 290px; left: 0; right: 0;
    text-align: center;
    font-size: 28px;
    font-weight: 600;
  }

  /* front */
  .front-brand {
    position: absolute;
    top: 150px; left: 50px; width: 420px;
    display: flex; align-items: center; justify-content: center; gap: 14px;
  }
  .front-brand .brand-dot { width: 40px; height: 40px; }
  .front-brand .brand-name { font-size: 28px; }
  .accent-bar {
    position: absolute;
    left: 0; top: 300px;
    width: 22px; height: 88px;
    background: var(--navy);
  }
  .holder {
    position: absolute;
    top: 290px; left: 40px; width: 430px;
    text-align: right;
    font-weight: 700;
    color: var(--navy-dark);
    font-size: 34px;
    line-height: 1.15;
    white-space: nowrap;
  }
  .contact-panel {
    position: absolute;
    top: 0; right: 0; bottom: 0;
    width: 400px;
    background: var(--panel);
    box-shadow: -6px 0 12px rgba(0,0,0,0.06);
    padding: 62px 20px 0 34px;
  }
  .contact-group {
    position: relative;
    padding-left: 40px;
    margin-bottom: 34px;
    font-size: 20px;
    line-height: 1.22;
    white-space: nowrap;
  }
  .contact-group h3 { font-size: 20px; font-weight: 700; }
  .contact-group .icon {
    position: absolute; left: 0; top: 52px;
    width: 24px; height: 24px;
    fill: var(--icon);
  }
  .contact-row { display: flex; }
  .contact-row span:first-child { width: 78px; }
  .contact-group--web { font-size: 16px; }
  .contact-group--web .icon { top: 38px; }
</style>
</head>
<body>

<section class="card card--back">
  <div class="world-map" role="img" aria-label="Faint dotted world map background"></div>
  <div class="back-brand">
    <span class="brand-dot"></span>
    <span class="brand-name">KV Holding Group LLC</span>
  </div>
  <p class="back-web">www.kvholdinggroup.example</p>
</section>

<section class="card card--front">
  <div class="world-map" role="img" aria-label="Faint dotted world map background"></div>
  <div class="front-brand">
    <span class="brand-dot"></span>
    <span class="brand-name">KV Holding Group LLC</span>
  </div>
  <div class="accent-bar"></div>
  <div class="holder">
    <p>Dorian P. Kell, CPA MST</p>
    <p>Principal</p>
  </div>

  <aside class="contact-panel">
    <div class="contact-group">
      <h3>Address</h3>
      <svg class="icon" viewBox="0 0 24 24" aria-hidden="true"><circle cx="12" cy="7" r="5"/><path d="M2 23c0-6 4-9 10-9s10 3 10 9z"/></svg>
      <p>418 East Marlow Avenue,</p>
      <p>Suite 7B</p>
      <p>Chicago, Illinois 60617</p>
    </div>
    <div class="contact-group">
      <h3>Mobile</h3>
      <svg class="icon" viewBox="0 0 24 24" aria-hidden="true"><rect x="6" y="1" width="12" height="22" rx="2"/><rect x="8" y="4" width="8" height="13" fill="#f4f4f5"/></svg>
      <p class="contact-row"><span>Phone:</span><span>312-555-0142</span></p>
      <p class="contact-row"><span>Mobile:</span><span>312-555-0167</span></p>
      <p class="contact-row"><span>Fax:</span><span>312-555-0188</span></p>
    </div>
    <div class="contact-group contact-group--web">
      <h3>Web</h3>
      <svg class="icon" viewBox="0 0 24 24" aria-hidden="true"><path d="M6 19a5 5 0 0 1-.5-10A7 7 0 0 1 19 9.5 4.75 4.75 0 0 1 18.5 19z"/></svg>
      <p>dorianpkell@kvholdinggroup.example</p>
      <p>www.kvholdinggroup.example</p>
    </div>
  </aside>
</section>

</body>
</html>
```